Launch Website

A very simple, but attractive website (template preferred) is required in a common format - HTML5 or Wordpress etc.
It should be easily user updateable for updates.
Pages it needs:
-Home Page with menu bar, company logo and 1 large graphic/picture and two smaller graphics/logos.
- What we do
- How we do it
- About Us
- Guarantees
- Results
- Contact Page with Enquiry Form
- Provision for a blog to be added later

Most pages will be approx 150 words text with some small/medium images.
We have our own domain & hosting.

A "less is more" design approach would be encouraged.

Target Market(s)

Vehicle Fleet Managers

Industry/Entity Type

It Company

Font styles to use
Sans Serif

Colors
9bcb3c

Requirements
Must have
• Corporate Style. No Fluff.
Nice to have
• Images of LIght Commerical vehicles and trucks

Am ok with white background throughout site.
Colours should match/complement company logo.
Should not have
• Should not be too "busy"

```html
<!DOCTYPE html>
<html lang="en">
<head>
<meta charset="utf-8">
<title>Tealvance – Fleet Engine Optimisation</title>
<link href="https://fonts.googleapis.com/css2?family=Open+Sans:wght@400;600&family=Titillium+Web:wght@400;600&display=swap" rel="stylesheet">
<style>
:root{
  --brand-blue:#1a9ad6;
  --band-top:#1b4f86;
  --band-bottom:#0f3e72;
  --accent-yellow:#f1e12a;
  --ink:#2b2b2b;
  --muted:#8c8c8c;
  --rule:#dcdcdc;
  --phone-red:#e0262b;
  --button:#c9c9c9;
  --footer-bg:#efefef;
  --white:#ffffff;
}
*{margin:0;padding:0;box-sizing:border-box}
html,body{width:1200px;height:1003px;overflow:hidden;background:var(--white)}
body{position:relative;font-family:"Open Sans",Arial,sans-serif;color:var(--ink)}

.site-header{position:absolute;left:0;top:0;width:1200px;height:103px;background:linear-gradient(#ffffff,#f2f2f2)}
.brand{position:absolute;left:131px;top:28px;display:flex;align-items:center;gap:10px}
.brand-mark{width:40px;height:40px;border-radius:50%;background:var(--brand-blue)}
.brand-name{font-family:"Titillium Web",Arial,sans-serif;font-weight:600;font-size:32px;color:var(--brand-blue);line-height:1}

.contact-box{position:absolute;left:810px;top:26px;display:flex;gap:10px}
.contact-icon{width:34px;height:52px}
.contact-lines{font-size:14px;color:var(--muted);line-height:19px}
.contact-lines .phone{color:var(--phone-red);font-size:20px;font-weight:400}
.contact-lines .email{color:var(--ink)}

.band{position:absolute;left:0;top:103px;width:1200px;height:441px;background:linear-gradient(var(--band-top),var(--band-bottom) 30%)}
.main-nav{position:absolute;left:140px;top:103px;height:44px;display:flex;gap:0}
.main-nav a{font-family:"Titillium Web",Arial,sans-serif;font-weight:600;font-size:15px;color:var(--white);text-decoration:none;text-transform:uppercase;line-height:44px;margin-right:34px}

.hero{position:absolute;left:131px;top:155px;width:937px;height:460px;background:var(--white);padding:9px;box-shadow:0 26px 18px -16px rgba(0,0,0,.35)}
.hero-photo{position:absolute;left:9px;top:9px;width:919px;height:449px;background:linear-gradient(180deg,#8fb0d4 0%,#d8e4ef 35%,#eef2f6 55%,#b9c6d3 72%,#8d8d86 100%)}
.hero-vehicle{position:absolute;left:495px;top:5px;width:380px;height:440px;background:linear-gradient(180deg,#d9d9d6 0%,#e9d832 30%,#d9c620 60%,#3c3c3c 100%);border-radius:6px}
.hero-band{position:absolute;left:9px;top:194px;width:460px;height:78px;background:var(--accent-yellow)}
.hero-band-right{position:absolute;left:893px;top:194px;width:35px;height:78px;background:var(--accent-yellow)}
.hero-copy{position:absolute;left:110px;top:0;font-family:"Titillium Web",Arial,sans-serif;color:var(--ink)}
.hero-lead{position:absolute;top:162px;left:0;font-size:24px;white-space:nowrap}
.hero-title{position:absolute;top:194px;left:0;text-transform:uppercase;white-space:nowrap;line-height:1}
.hero-title .small{display:block;font-size:34px;margin-top:4px}
.hero-title .big{display:block;font-size:47px;margin-top:-2px}
.hero-tail{position:absolute;top:275px;left:0;font-size:24px;white-space:nowrap}
.hero-arrow{position:absolute;top:208px;width:28px;height:50px}
.hero-arrow.prev{left:17px}
.hero-arrow.next{left:891px}
.partner-badges{position:absolute;left:105px;top:375px;display:flex;gap:3px}
.partner-badge{width:123px;height:56px;background:var(--white);display:flex;align-items:center;justify-content:center}
.partner-badge span{display:block;width:80px;height:22px;border-radius:3px}
.partner-badge.one span{background:#2a3d78}
.partner-badge.two span{background:#3a9a3a}

.features{position:absolute;left:131px;top:680px;display:flex;gap:37px}
.feature{width:206px}
.feature h2{font-family:"Titillium Web",Arial,sans-serif;font-weight:400;font-size:21px;color:var(--brand-blue);text-transform:uppercase;line-height:24px}
.feature .rule{position:relative;height:2px;background:var(--rule);margin:9px 0 16px}
.feature .rule::before{content:"";position:absolute;left:0;top:0;width:84px;height:2px;background:var(--brand-blue)}
.feature p{font-size:12.5px;line-height:19px;color:var(--muted);height:96px}
.feature .more{display:inline-block;margin-top:10px;background:var(--button);color:var(--white);font-size:11.5px;line-height:24px;padding:0 10px;border-radius:2px;text-decoration:none}

.site-footer{position:absolute;left:0;top:923px;width:1200px;height:80px;background:var(--footer-bg)}
.legal{position:absolute;left:131px;top:20px;font-size:13px;line-height:19px;color:var(--muted)}
.legal a{color:var(--muted);text-decoration:none}
.social{position:absolute;left:960px;top:26px;display:flex;gap:9px}
.social a{display:block;width:30px;height:30px;border-radius:2px}
.social .s1{background:#3b5998}
.social .s2{background:#1da1f2}
.social .s3{background:#0e76a8}
</style>
</head>
<body>

<header class="site-header">
  <div class="brand">
    <span class="brand-mark"></span>
    <span class="brand-name">Tealvance</span>
  </div>
  <div class="contact-box">
    <svg class="contact-icon" viewBox="0 0 34 52" aria-hidden="true">
      <path d="M14 2c-6 2-8 8-8 18s3 18 9 22c2 1 4 0 5-2l-4-7c-1-1-3-1-4 0-2-4-2-14 0-18 1 1 3 1 4 0l3-8c1-2-1-6-5-5z" fill="#2b2b2b"/>
      <path d="M15 43c4 5 12 6 17 4" stroke="#2b2b2b" stroke-width="1.5" fill="none"/>
    </svg>
    <div class="contact-lines">
      <div>Contact us on <span class="phone">(02) 5550 1234</span></div>
      <div>or email us <span class="email">info@tealvance.com</span></div>
    </div>
  </div>
</header>

<div class="band"></div>
<nav class="main-nav">
  <a href="#">Home</a>
  <a href="#">What we do</a>
  <a href="#">How we do it</a>
  <a href="#">About us</a>
  <a href="#">Guarantees</a>
  <a href="#">Results</a>
  <a href="#">Testimonials</a>
  <a href="#">Contact</a>
  <a href="#">Blog</a>
</nav>

<section class="hero">
  <div class="hero-photo" role="img" aria-label="Yellow refrigerated truck driving on an open road under a cloudy sky">
    <div class="hero-vehicle"></div>
  </div>
  <div class="hero-band"></div>
  <div class="hero-band-right"></div>
  <div class="hero-copy">
    <p class="hero-lead">We help diesel vehicle fleets</p>
    <h1 class="hero-title"><span class="small">Save up to</span><span class="big">20% fuel costs</span></h1>
    <p class="hero-tail">by optimising their engines.</p>
  </div>
  <svg class="hero-arrow prev" viewBox="0 0 28 50" aria-hidden="true"><path d="M26 2 2 25l24 23" stroke="#555" stroke-width="1.5" fill="none"/></svg>
  <svg class="hero-arrow next" viewBox="0 0 28 50" aria-hidden="true"><path d="M2 2l24 23L2 48" stroke="#555" stroke-width="1.5" fill="none"/></svg>
  <div class="partner-badges">
    <div class="partner-badge one" role="img" aria-label="Industry association member badge"><span></span></div>
    <div class="partner-badge two" role="img" aria-label="Fairway Fleet partner badge"><span></span></div>
  </div>
</section>

<main class="features">
  <article class="feature">
    <h2>About us</h2>
    <div class="rule"></div>
    <p>Fairway Fleet have combined over 50years experience in all aspects of the automotive industry including commercial fleet and diesel engines. We are the ...</p>
    <a class="more" href="#">Read More</a>
  </article>
  <article class="feature">
    <h2>What we do</h2>
    <div class="rule"></div>
    <p>Fairway Fleet delivers award winning, ISO 9001 certified diesel engine ECU remapping for fleet operations. As Principal Australian Fleet Agent for Tealvance...</p>
    <a class="more" href="#">Read More</a>
  </article>
  <article class="feature">
    <h2>How we do it</h2>
    <div class="rule"></div>
    <p>Fairway Fleet will conduct an obligation Free Consultation with your Fleet Representatives to determine your Fleets needs, and identify any customization...</p>
    <a class="more" href="#">Read More</a>
  </article>
  <article class="feature">
    <h2>Why</h2>
    <div class="rule"></div>
    <p>We've acted on customer requests for cost effective, financially attractive solutions to reduce fuel and operating costs whilst also reducing environmental foot...</p>
    <a class="more" href="#">Read More</a>
  </article>
</main>

<footer class="site-footer">
  <div class="legal">
    <div>Copyright 2014 tealvance. All Rights Reserved.</div>
    <div><a href="#">Privacy Policy</a> | <a href="#">Terms and Conditions</a></div>
  </div>
  <div class="social">
    <a class="s1" href="#" aria-label="Social profile one"></a>
    <a class="s2" href="#" aria-label="Social profile two"></a>
    <a class="s3" href="#" aria-label="Social profile three"></a>
  </div>
</footer>

</body>
</html>
```